I am a Financial Adviser specialising in Aged Care Advice. We provide financial advice and assistance to families with loved ones entering an Aged Care facility.
We need a flyer detailing the Aged Care Packages that we offer. There will be 3 main packages & then other add ons. I need an area where the client can sign off on the package/s that they choose. I have attached a sample to demonstrate the required layout, and a copy of content. I would like the flyer to have an image as per the attached sample, and to be designed in soft pastels, blues, greens.

Financial

```html
<!DOCTYPE html>
<html lang="en">
<head>
<meta charset="utf-8">
<title>Aged Care Services – Harbourline Advisory</title>
<link rel="stylesheet" href="https://fonts.googleapis.com/css2?family=Open+Sans:ital,wght@0,400;0,600;0,700;1,300;1,400&family=Playfair+Display:ital@1&display=swap">
<style>
:root{
  --page-bg:#ffffff;
  --sage:#dde1dc;
  --sage-deep:#d6dad4;
  --blue:#bac4d6;
  --gold:#d4b978;
  --gold-head:#d3b86f;
  --footer:#7d8aa6;
  --ink:#1d1d1d;
  --body:#2f2f2f;
  --serif-brown:#6b4a2c;
  --muted:#555;
  --rule:#b7a27a;
}
*{box-sizing:border-box;margin:0;padding:0}
html,body{width:1200px;height:900px;overflow:hidden;background:#fff}
body{position:relative;font-family:"Open Sans",Arial,sans-serif;color:var(--body)}
.page{position:absolute;top:44px;width:565px;height:799px;background:var(--page-bg);box-shadow:3px 4px 8px rgba(0,0,0,.25);overflow:hidden}
.page--front{left:26px}
.page--back{left:617px}

/* front */
.hero{position:absolute;left:0;top:0;width:565px;height:306px;background:radial-gradient(ellipse at 60% 40%,#e9d3bf 0%,#c89c7f 45%,#a9805f 75%,#d8dcc4 100%)}
.brand{position:absolute;left:18px;top:36px;display:flex;align-items:center;gap:8px}
.brand__dot{width:12px;height:12px;border-radius:50%;background:var(--gold)}
.brand__name{font-family:"Open Sans",Arial,sans-serif;font-weight:700;font-size:17px;color:var(--ink)}
.title-band{position:absolute;left:0;top:306px;width:565px;height:60px;background:linear-gradient(90deg,#eee2cf,#f6efe4 50%,#eadcc7)}
.title-band h1{font-family:"Playfair Display",Georgia,serif;font-style:italic;font-weight:400;font-size:38px;color:var(--serif-brown);position:absolute;left:120px;top:4px}
.col{position:absolute;top:366px;height:433px;padding:28px 12px 0 16px}
.col--essentials{left:0;width:188px;background:var(--sage)}
.col--advantage{left:188px;width:188px;background:var(--blue)}
.col--platinum{left:376px;width:189px;background:var(--gold)}
.col__theme{font-family:"Playfair Display",Georgia,serif;font-style:italic;font-size:24px;color:#8a6a45;text-align:center;border-bottom:1px solid var(--rule);padding-bottom:0;margin:0 6px}
.col__lead{font-style:italic;font-weight:300;font-size:13px;color:#444;text-align:center;line-height:16px;margin-top:4px;height:70px}
.package{display:flex;gap:8px;margin-top:0}
.tick-box{width:22px;height:22px;background:#fff;border:1px solid #999;flex:none;margin-top:2px}
.package__name{font-weight:600;font-size:13px;color:var(--ink);line-height:17px}
.package__plus{font-weight:600;font-size:9.5px;color:var(--ink);margin:3px 0 6px}
.features{list-style:none;font-size:9.5px;line-height:13.5px;color:var(--body)}
.note{font-size:8px;line-height:11px;margin-top:12px;color:var(--body)}

/* back */
.options-head{position:absolute;left:0;top:0;width:565px;height:46px;background:var(--gold-head)}
.options-head h2{font-family:"Playfair Display",Georgia,serif;font-style:italic;font-weight:400;font-size:24px;color:#fff;position:absolute;left:90px;top:8px}
.options-area{position:absolute;left:0;top:46px;width:378px;height:450px;background:var(--sage-deep)}
.options-strip{position:absolute;left:378px;top:46px;width:187px;height:450px;background:var(--blue)}
.options-photo{position:absolute;left:366px;top:163px;width:183px;height:183px;border:3px solid #fff;background:linear-gradient(135deg,#7f9a52,#c8c6b9 45%,#8a8fa0 80%,#d0c2b4)}
.option-list{position:absolute;left:33px;top:56px;width:330px;list-style:none}
.option{margin-bottom:17px}
.option__head{display:flex;align-items:center;gap:6px}
.option__head .tick-box{width:17px;height:17px;margin:0}
.option__name{font-weight:600;font-size:11.5px;color:var(--ink)}
.option__desc{font-size:8.7px;line-height:12px;color:var(--body);margin-top:1px}
.agreement{position:absolute;left:33px;top:504px;width:500px;font-size:11px;line-height:16px;color:var(--body)}
.agreement__rule{position:absolute;left:36px;top:592px;width:494px;height:1px;background:#b8bfcc}
.sign{position:absolute;font-size:11px;color:var(--body)}
.sign__line{letter-spacing:1px;color:#666;font-size:9px}
.footer{position:absolute;left:0;top:708px;width:565px;height:91px;background:var(--footer);padding:7px 36px;color:#eef0f5;font-size:7.6px;line-height:10px}
.footer em{font-size:9px}
</style>
</head>
<body>

<section class="page page--front">
  <div class="hero" role="img" aria-label="Photo of a young hand gently holding an elderly hand"></div>
  <div class="brand"><span class="brand__dot"></span><span class="brand__name">Harbourline Advisory</span></div>
  <div class="title-band"><h1>Aged Care Services</h1></div>

  <div class="col col--essentials">
    <p class="col__theme">Peace of Mind</p>
    <p class="col__lead">When you know<br>what you want</p>
    <div class="package"><span class="tick-box"></span><p class="package__name">ESSENTIALS Package<br>$770</p></div>
    <ul class="features" style="margin-top:8px">
      <li>Explanation of Aged Care Fees and Charges.</li>
      <li>Preliminary Home/Assets Assessment.*</li>
      <li>Estimated Means Tested Fee Calculation.*</li>
      <li>Preliminary Aged Care Costs.*</li>
      <li>Estimated Cash Flow Scenario.*</li>
    </ul>
    <p class="note">*Please note this is general factual information only.<br>We do not provide any specific personal information.</p>
  </div>

  <div class="col col--advantage">
    <p class="col__theme">Confidence</p>
    <p class="col__lead">When you need to know<br>all the options</p>
    <div class="package"><span class="tick-box"></span><p class="package__name">ADVANTAGE Package<br>$2,970</p></div>
    <p class="package__plus">ESSENTIALS Package plus</p>
    <ul class="features">
      <li>Analyse and Strategize Aged Care costs.</li>
      <li>Compare up to 5 Strategy options.</li>
      <li>Minimise Aged Care Costs (where possible).</li>
      <li>Maximise Age Pension Income (where possible).</li>
      <li>Prepare a Full Statement of Advice (SOA).</li>
      <li>Implementation of Aged Care Strategy.</li>
    </ul>
  </div>

  <div class="col col--platinum">
    <p class="col__theme">Convenience</p>
    <p class="col__lead">When you need someone<br>to take charge</p>
    <div class="package"><span class="tick-box"></span><p class="package__name">PLATINUM Package<br>$5,940</p></div>
    <p class="package__plus">ADVANTAGE Package plus</p>
    <ul class="features">
      <li>Liase with the Aged Care Facility.</li>
      <li>Pension Office Nominee.</li>
      <li>Post Entry Review.</li>
      <li>Post Implementation SOA (if required).</li>
      <li>Annual Review.</li>
    </ul>
  </div>
</section>

<section class="page page--back">
  <div class="options-head"><h2>Extra Choice Options</h2></div>
  <div class="options-area"></div>
  <div class="options-strip"></div>
  <div class="options-photo" role="img" aria-label="Photo of a carer chatting with a smiling elderly woman outdoors"></div>

  <ul class="option-list">
    <li class="option"><div class="option__head"><span class="tick-box"></span><span class="option__name">Pension Office Nominee $1,100</span></div>
      <p class="option__desc">Communicate with the Pension Office on behalf of our client/s, and undertake all changes and updates to details, as directed by our client.</p></li>
    <li class="option"><div class="option__head"><span class="tick-box"></span><span class="option__name">Post Implementation Statement of Advice $1,650</span></div>
      <p class="option__desc">Revise our original Advice Statement for any changes of circumstances including income &amp; asset variations, and provide further advice within the first 12 months of initial advice statement.</p></li>
    <li class="option"><div class="option__head"><span class="tick-box"></span><span class="option__name">Annual Review $990</span></div>
      <p class="option__desc">A review of the recommendations made in our original advice document, taking into account any changes to client's circumstances including checking current cash flow is sufficient to meet ongoing aged care costs.</p></li>
    <li class="option"><div class="option__head"><span class="tick-box"></span><span class="option__name">Post Entry Review $660</span></div>
      <p class="option__desc">Review financial situation, check facility invoices are accurate, explain the Residential Aged Care Agreement and ensure all recommendations are implemented.</p></li>
    <li class="option"><div class="option__head"><span class="tick-box"></span><span class="option__name">Facility Liason $550</span></div>
      <p class="option__desc">Negotiate with the Aged Care Facility regarding Accommodation payments, clarify &amp; explain Residential Care Agreement, and review facility invoices.</p></li>
    <li class="option"><div class="option__head"><span class="tick-box"></span><span class="option__name">Family Conferences $660</span></div>
      <p class="option__desc">Facilitate &amp; co-ordinate family meetings to explain the Aged Care legislation and how it fits with the family circumstances.</p></li>
    <li class="option"><div class="option__head"><span class="tick-box"></span><span class="option__name">Estate Wrap $660</span></div>
      <p class="option__desc">Assist beneficiaries with correct procedures and paperwork regarding the finalisation of the estate.</p></li>
  </ul>

  <div class="agreement">
    <p>I/We have chosen the Service Package and Options as ticked above.</p>
    <p>I/We understand that by choosing the Essentials Package, that I/We are receiving factual information only, and not financial advice.</p>
    <p>I/We agree to pay the amount of ………………….,&nbsp;&nbsp;&nbsp;within seven days of the date of the invoice received from Harbourline Advisory.</p>
  </div>
  <div class="agreement__rule"></div>

  <div class="sign" style="left:36px;top:620px"><p class="sign__line">……………………………………</p><p>Signature</p></div>
  <div class="sign" style="left:190px;top:620px"><p class="sign__line">……………………………………</p><p>Signature</p></div>
  <div class="sign" style="left:334px;top:620px"><p class="sign__line">……………………………………</p><p>Signature</p></div>
  <div class="sign" style="left:478px;top:620px"><p class="sign__line">……./……../………</p><p>Date</p></div>
  <div class="sign" style="left:36px;top:668px"><p class="sign__line">……………………………………</p><p>Adviser Signature</p></div>
  <div class="sign" style="left:196px;top:668px"><p class="sign__line">………/………/………</p><p>Date</p></div>

  <div class="footer">
    <p><em>Important Information</em></p>
    <p>This document has been prepared by Harbourline Advisory Pty Ltd ABN 00 000 000 000, an Authorised Representative of Meridian Licensee Limited ABN 00 000 000 000 AFSL 000000, a wholly owned, non-guaranteed subsidiary of the Southern Cross Banking Group ABN 00 000 000 000.</p>
    <p>Information in this document is based on current regulatory requirements and laws, as at 20 September, 2016 which may be subject to change. It contains general advice. It does not take into account your individual objectives, financial situation or needs. You should consider talking to a financial adviser before making a financial decision.</p>
  </div>
</section>

</body>
</html>
```